Visitenkarten-Design für Gesundheits- und Ernährungsberaterin
Zielgruppe
Ich bin Gesundheit und Ernährungsberaterin
Zielgruppe sind chronisch Kranke und Gesundheitsbewusste Personen
Aufgabenstellung
Schlichtes aber direkt erkennbares Design.
Mahl mit Maß , Gesundheit und Ernährungsberatung ( gut lesbar , elegant)
Marlene Obruk-Feistinger ( nicht so groß )
Grau ; Grün Töne und gerne etwas rosa
Infos wie Adresse und E-Mail vielleicht in jeweilige Blöcke am unteren Rand

```html
<!DOCTYPE html>
<html lang="de">
<head>
<meta charset="utf-8">
<title>Visitenkarten – Mahl mit Maß</title>
<link href="https://fonts.googleapis.com/css2?family=Open+Sans:wght@400&family=Carlito&family=Dancing+Script:wght@500&display=swap" rel="stylesheet">
<style>
  :root {
    --rose: #f9a8a8;
    --green: #8ccf5f;
    --green-text: #7fc650;
    --green-pale: #c5e8ad;
    --green-fill: #8dd35f;
    --paper: #ffffff;
    --page: #ffffff;
  }
  * { box-sizing: border-box; margin: 0; padding: 0; }
  html, body { width: 861px; height: 1200px; overflow: hidden; background: var(--page); }
  .sheet { position: relative; width: 861px; height: 1200px; }
  .accent-bar { position: absolute; left: 793px; top: 155px; width: 5px; height: 108px; background: var(--green-pale); }

  .card {
    position: absolute; width: 335px; height: 216px; background: var(--paper);
    box-shadow: 3px 4px 7px rgba(0,0,0,.32); overflow: hidden;
    font-family: "Carlito", "Calibri", sans-serif; color: var(--green-text);
  }
  .card::before { content: ""; position: absolute; left: 0; top: 0; bottom: 0; width: 10px; background: var(--stripe); }
  .card--rose { --stripe: var(--rose); --mark: 249,168,168; }
  .card--green { --stripe: var(--green-pale); --mark: 197,232,173; }
  .card--solid { background: var(--green-fill); }

  .col-left { left: 63px; } .col-right { left: 433px; }
  .row-1 { top: 188px; } .row-2 { top: 474px; } .row-3 { top: 771px; }

  .mark {
    position: absolute; border-radius: 48% 48% 50% 50%;
    background: radial-gradient(ellipse at 50% 45%, rgba(var(--mark), .35), rgba(var(--mark), 0) 72%);
  }
  .card--solid .mark { background: radial-gradient(ellipse at 50% 45%, rgba(197,232,173,.45), rgba(197,232,173,0) 72%); }

  .slogan { position: absolute; font-family: "Open Sans", sans-serif; letter-spacing: 1.6px; line-height: 1.1; white-space: nowrap; }
  .slogan--long { text-align: center; }
  .slogan--script { font-family: "Dancing Script", cursive; letter-spacing: 0; }

  .name { position: absolute; left: 18px; font-size: 13.5px; white-space: nowrap; }
  .role { position: absolute; left: 18px; font-size: 9px; white-space: nowrap; }
  .address { position: absolute; left: 18px; top: 186px; font-size: 9px; line-height: 12.3px; }
  .contact { position: absolute; left: 183px; top: 174px; font-size: 9px; line-height: 12.3px; display: grid; grid-template-columns: 33px auto; }
</style>
</head>
<body>
<div class="sheet">
  <div class="accent-bar"></div>

  <!-- Reihe 1: rosa -->
  <section class="card card--rose col-left row-1">
    <div class="mark" role="img" aria-label="Apfel-Logo der Beratung" style="left:173px;top:24px;width:122px;height:158px"></div>
    <p class="slogan slogan--long" style="left:0;right:0;padding-left:16px;top:102px;font-size:14.5px;width:330px;">Mahl mit Maß, Gesundheits-<br>und Ernährungsberatung.</p>
  </section>

  <section class="card card--rose col-right row-1">
    <div class="mark" role="img" aria-label="Apfel-Logo der Beratung" style="left:243px;top:5px;width:83px;height:108px"></div>
    <p class="slogan slogan--long" style="left:155px;top:59px;font-size:9.6px;letter-spacing:1px;width:160px;">Mahl mit Maß, Gesundheits-<br>und Ernährungsberatung.</p>
    <p class="name" style="top:136px">Marlene Obruk-Feistinger</p>
    <p class="address">Lindenstieg 4<br>24799 Moorbrück</p>
    <div class="contact"><span>TEL</span><span>04352 /726 41 19</span><span>MOBIL</span><span>0152 / 38 71 26 05</span><span>MAIL</span><span>beratung-mof@postfach.de</span></div>
  </section>

  <!-- Reihe 2: hellgrün -->
  <section class="card card--green col-left row-2">
    <div class="mark" role="img" aria-label="Apfel-Logo der Beratung" style="left:143px;top:31px;width:123px;height:160px"></div>
    <p class="slogan" style="left:74px;top:106px;font-size:22px;">Mahl mit Maß.</p>
  </section>

  <section class="card card--green col-right row-2">
    <div class="mark" role="img" aria-label="Apfel-Logo der Beratung" style="left:229px;top:5px;width:97px;height:126px"></div>
    <p class="slogan" style="right:17px;top:66px;font-size:17.5px;">Mahl mit Maß.</p>
    <p class="name" style="top:133px">Marlene Obruk-Feistinger</p>
    <p class="role" style="top:149px">Gesundheits- und Ernährungsberaterin</p>
    <p class="address">Lindenstieg 4<br>24799 Moorbrück</p>
    <div class="contact"><span>TEL</span><span>04352 /726 41 19</span><span>MOBIL</span><span>0152 / 38 71 26 05</span><span>MAIL</span><span>beratung-mof@postfach.de</span></div>
  </section>

  <!-- Reihe 3: Schreibschrift -->
  <section class="card card--green card--solid col-left row-3">
    <div class="mark" role="img" aria-label="Apfel-Logo der Beratung" style="left:127px;top:18px;width:143px;height:186px"></div>
    <p class="slogan slogan--script" style="left:76px;top:104px;font-size:25px;color:#fff;">Mahl mit Maß.</p>
  </section>

  <section class="card card--green col-right row-3">
    <div class="mark" role="img" aria-label="Apfel-Logo der Beratung" style="left:229px;top:5px;width:97px;height:127px"></div>
    <p class="slogan slogan--script" style="right:18px;top:63px;font-size:17px;">Mahl mit Maß.</p>
    <p class="name" style="top:133px">Marlene Obruk-Feistinger</p>
    <p class="role" style="top:149px">Gesundheits- und Ernährungsberaterin</p>
    <p class="address">Lindenstieg 4<br>24799 Moorbrück</p>
    <div class="contact"><span>TEL</span><span>04352 /726 41 19</span><span>MOBIL</span><span>0152 / 38 71 26 05</span><span>MAIL</span><span>beratung-mof@postfach.de</span></div>
  </section>
</div>
</body>
</html>
```